Tallow Ridge Craft Cannabis Company

We need a one-page website designed for a craft cannabis website called "Tallow Ridge is a craft cannabis company" that will provide high-quality strains. It's located on tallowridge in Abbotsford British Columbia on lush green acreage. The facility takes pride in its modern technology bloom rooms to contain a healthy environment for high-quality handcrafted cannabis. We need a design that looks modern yet rustic- please do not add any marijuana leaves- We want the site to look professional as it is for investors. we will be selling products and do need the site to say "Coming soon"
Target Market(s)
investors and customers
Number of Pages Required
1 page
Font styles to use
Colors
Designer to choose colors to be used in the design.
Requirements
Must have
- greenery- its a cannabis production site with state of the art technology for growing. from seeds to full production it is a craft site with smaller rooms but high-end quality products. we need a tab that has a purchasing section another one for investors to watch our market trends and a page with our mission/ values and visions-
Nice to have
- showing people/ high end images/ greenspace/ farm (horticulture based)
Should not have
- no marijuana leaves

```html
<!DOCTYPE html>
<html lang="en">
<head>
<meta charset="utf-8">
<title>Tallow Ridge Craft Cannabis Company</title>
<link href="https://fonts.googleapis.com/css2?family=Montserrat:wght@500;600;700;800&family=Open+Sans:wght@400;600&display=swap" rel="stylesheet">
<style>
:root{
  --green:#2f9a2a;
  --green-light:#6ccc45;
  --green-dark:#1f7a1c;
  --green-text:#2c8a26;
  --orange:#e08a10;
  --orange-dark:#c7730a;
  --ink:#1d1d1d;
  --body:#3a3a3a;
  --muted:#6f6f6f;
  --paper:#f6f2ea;
  --wood:#3a2a20;
  --wood-dark:#221812;
  --white:#ffffff;
}
*{box-sizing:border-box;margin:0;padding:0}
html,body{width:1200px;height:3267px;overflow:hidden}
body{position:relative;background:var(--white);font-family:"Open Sans",Arial,sans-serif;color:var(--body)}
.abs{position:absolute}
.head{font-family:"Montserrat",Arial,sans-serif;font-weight:700;text-transform:uppercase}

/* header */
.site-header{position:absolute;left:0;top:0;width:1200px;height:87px;background:var(--white);z-index:5}
.brand{position:absolute;left:180px;top:22px;display:flex;align-items:center;gap:12px}
.brand-dot{width:40px;height:40px;border-radius:50%;background:var(--green)}
.brand-name{font-family:"Montserrat",Arial,sans-serif;font-weight:700;font-size:28px;color:var(--green)}
.nav{position:absolute;top:36px;left:486px;display:flex;gap:0}
.nav a{font-family:"Open Sans",Arial,sans-serif;font-size:16px;color:var(--ink);text-decoration:none;text-transform:uppercase;position:absolute;white-space:nowrap}
.nav a.active{color:var(--green)}
.nav-mark{position:absolute;left:504px;top:20px;width:22px;height:9px;border-radius:50%;background:var(--green)}

/* hero */
.hero{position:absolute;left:0;top:87px;width:1200px;height:575px;background:radial-gradient(ellipse at 60% 45%,#2f6d78 0%,#1b4853 45%,#0f2a33 100%)}
.hero-title{position:absolute;top:200px;width:1200px;text-align:center;font-size:48px;color:var(--white);font-weight:700;letter-spacing:.5px}
.hero-sub{position:absolute;top:268px;left:270px;width:660px;text-align:center;font-size:21px;line-height:28px;color:#f1f5f6}
.btn-orange{position:absolute;background:var(--orange);color:var(--white);font-family:"Montserrat",Arial,sans-serif;font-weight:700;font-size:16px;text-transform:uppercase;display:flex;align-items:center;justify-content:center;letter-spacing:.3px}
.hero-edge{position:absolute;left:0;top:590px;width:1200px;height:80px}

/* paper sections */
.paper{position:absolute;left:0;width:1200px;background:linear-gradient(180deg,#f9f6f0 0%,#efe8da 50%,#f7f3eb 100%)}
.mission-photo{position:absolute;left:172px;top:730px;width:420px;height:340px;background:linear-gradient(135deg,#3b3b3b,#8c8f8a 55%,#2a2a2a);clip-path:polygon(50% 0,100% 50%,50% 100%,0 50%)}
.section-title{font-family:"Montserrat",Arial,sans-serif;font-weight:800;font-size:34px;text-transform:uppercase;color:var(--ink)}
.section-title .accent{color:var(--green-text)}
.lead{font-size:16px;line-height:24px;color:var(--ink)}
.copy{font-size:14px;line-height:28px;color:var(--muted)}
.btn-outline{position:absolute;border:2px solid var(--green);color:var(--green);font-family:"Montserrat",Arial,sans-serif;font-weight:700;font-size:16px;text-transform:uppercase;display:flex;align-items:center;justify-content:center}

/* products */
.products-band{position:absolute;left:0;top:1120px;width:1200px;height:610px}
.products-title{position:absolute;top:1222px;width:1200px;text-align:center;color:var(--white);font-size:31px}
.product-card{position:absolute;top:1300px;width:200px;height:197px;border-radius:0 40px 0 40px;overflow:hidden}
.product-card.soon{background:var(--ink);display:flex;align-items:center;justify-content:center;text-align:center;color:var(--white);font-family:"Montserrat",Arial,sans-serif;font-weight:800;font-size:20px;line-height:21px}
.product-info{position:absolute;top:1514px;width:200px;text-align:center;color:var(--white)}
.product-name{font-size:16px;text-transform:uppercase;letter-spacing:.3px}
.product-desc{font-size:12px;line-height:15px;margin-top:3px;color:#eef8e8}
.chev{position:absolute;top:1580px;width:36px;height:36px;border-radius:50%;background:var(--white)}
.arrow{position:absolute;top:1400px;width:44px;height:26px}

/* greenery */
.greenery-photo{position:absolute;left:400px;top:1690px;width:800px;height:515px;background:linear-gradient(90deg,rgba(255,255,255,1) 0%,rgba(214,196,150,.6) 22%,#b98a44 45%,#6e8a33 70%,#4a3016 100%)}

/* newsletter */
.news-title{position:absolute;top:2296px;width:1200px;text-align:center;color:var(--green-text);font-size:29px}
.news-copy{position:absolute;top:2347px;left:290px;width:620px;text-align:center;font-size:15px;line-height:25px;color:var(--body)}
.news-form{position:absolute;left:288px;top:2426px;width:640px;height:62px;border-radius:31px;background:var(--white);border:2px solid #e0ded8}
.news-placeholder{position:absolute;left:38px;top:20px;font-size:15px;color:#555;text-transform:uppercase}
.news-submit{position:absolute;right:8px;top:8px;width:144px;height:42px;border-radius:21px;background:var(--green-dark);color:var(--white);font-family:"Montserrat",Arial,sans-serif;font-weight:700;font-size:16px;text-transform:uppercase;display:flex;align-items:center;justify-content:center}

/* contact */
.contact{position:absolute;left:0;top:2560px;width:1200px;height:575px;background:linear-gradient(180deg,var(--wood) 0%,#2c1f17 60%,var(--wood) 100%)}
.contact-title{position:absolute;top:2676px;width:1200px;text-align:center;color:var(--white);font-size:30px}
.field{position:absolute;left:190px;width:400px;border-bottom:1px solid #9a8f86;color:var(--white);font-size:16px;padding-left:10px}
.btn-submit{position:absolute;left:190px;top:2974px;width:145px;height:46px;border-radius:23px;background:var(--green);color:var(--white);font-family:"Montserrat",Arial,sans-serif;font-weight:700;font-size:16px;text-transform:uppercase;display:flex;align-items:center;justify-content:center}
.info{position:absolute;left:684px;color:var(--white);font-size:16px;line-height:21px;text-transform:uppercase}
.info .val{text-transform:none}
.info-icon{position:absolute;left:636px;width:30px;height:30px}
.social{position:absolute;top:2972px;width:38px;height:38px;border-radius:50%;border:2px solid var(--white)}

/* footer */
.site-footer{position:absolute;left:0;top:3133px;width:1200px;height:134px;background:#1b1410}
.footer-nav{position:absolute;top:40px;width:1200px;text-align:center}
.footer-nav a{color:var(--white);text-decoration:none;font-size:17px;text-transform:uppercase;margin:0 20px}
.footer-copy{position:absolute;top:78px;width:1200px;text-align:center;color:#8d847c;font-size:12px}
</style>
</head>
<body>

<header class="site-header">
  <div class="brand"><span class="brand-dot"></span><span class="brand-name">TALLOW RIDGE</span></div>
  <span class="nav-mark"></span>
  <nav class="nav">
    <a class="active" href="#" style="left:0">Home</a>
    <a href="#" style="left:103px">About</a>
    <a href="#" style="left:212px">Shop</a>
    <a href="#" style="left:311px">Investors</a>
    <a href="#" style="left:455px">Mission</a>
  </nav>
</header>

<section class="hero" role="img" aria-label="Gloved hand holding a cannabis bud over a teal medical data display"></section>
<h1 class="abs head hero-title" style="top:287px;z-index:2">Welcome to Tallow Ridge</h1>
<p class="hero-sub" style="top:355px;z-index:2">Morbi porta libero id ullamcorper nonummy nibh ligula pulvinar metus eget consectetuer augue nisi quis lacu</p>
<a class="btn-orange" style="left:508px;top:440px;width:182px;height:50px;z-index:2">Learn More</a>

<section class="paper" style="top:640px;height:560px"></section>
<svg class="hero-edge" viewBox="0 0 1200 80" preserveAspectRatio="none" aria-hidden="true">
  <path d="M0 40 L40 22 L80 48 L130 18 L170 44 L220 26 L260 50 L310 20 L360 46 L410 24 L460 52 L500 28 L550 46 L600 22 L650 50 L700 26 L750 48 L800 20 L850 44 L900 24 L950 52 L1000 26 L1050 46 L1100 20 L1150 42 L1200 28 L1200 80 L0 80 Z" fill="#f8f5ee"/>
</svg>

<section class="mission">
  <div class="mission-photo" role="img" aria-label="Grower inspecting plants, framed in a diamond shape"></div>
  <h2 class="abs section-title" style="left:598px;top:737px">Our <span class="accent">Mission</span></h2>
  <p class="abs lead" style="left:600px;top:798px;width:420px">Integer congue augue et malesuada iaculis ipsum dui aliquet felis at cursus magna nisl nec elit</p>
  <p class="abs copy" style="left:600px;top:858px;width:430px">Aliquam sit amet porttitor mattis enim in massa libero interdum nec interdum vel blandit sed nulla in ullamcorper est eget tempor cursus neque mi consectetuer mi a ultricies massa est sed nisl Class aptent taciti sociosqu ad litora</p>
  <a class="btn-outline" style="left:603px;top:1008px;width:175px;height:44px">Read More</a>
</section>

<svg class="products-band" viewBox="0 0 1200 610" preserveAspectRatio="none" aria-hidden="true">
  <defs>
    <linearGradient id="bandGreen" x1="0" y1="0" x2="1" y2="0">
      <stop offset="0" stop-color="#2a8f25"/><stop offset="1" stop-color="#72d048"/>
    </linearGradient>
  </defs>
  <path d="M0 80 L1200 10 L1200 600 L0 545 Z" fill="url(#bandGreen)"/>
</svg>
<h2 class="abs head products-title">Our Products</h2>
<svg class="arrow" style="left:106px" viewBox="0 0 44 26" aria-hidden="true"><path d="M42 13 H4 M14 3 L4 13 L14 23" stroke="#fff" stroke-width="3" fill="none"/></svg>
<svg class="arrow" style="left:1036px" viewBox="0 0 44 26" aria-hidden="true"><path d="M2 13 H40 M30 3 L40 13 L30 23" stroke="#fff" stroke-width="3" fill="none"/></svg>

<div class="product-card" style="left:182px;background:linear-gradient(160deg,#c9b7a2,#6d4a2c 60%,#3a2818)" role="img" aria-label="Dried cannabis buds on linen"></div>
<div class="product-card" style="left:395px;background:linear-gradient(160deg,#e9e6dc,#8aa04a 45%,#b23a22 75%,#d79a2a)" role="img" aria-label="Cannabis buds beside bottles of oil"></div>
<div class="product-card" style="left:607px;background:linear-gradient(160deg,#ddd6c6,#6f8c3a 50%,#b97a2a 80%,#7a5a30)" role="img" aria-label="Oil bottles and buds on a wooden table"></div>
<div class="product-card soon">COMING<br>SOON</div>
<style>.product-card.soon{left:820px}</style>

<div class="product-info" style="left:176px"><div class="product-name">Product Title</div><div class="product-desc">Atetuer mi a ultricies massa<br>est sed nisl Class aptent</div></div>
<div class="product-info" style="left:402px"><div class="product-name">Product Title</div><div class="product-desc">Atetuer mi a ultricies massa<br>est sed nisl Class aptent</div></div>
<div class="product-info" style="left:612px"><div class="product-name">Product Title</div><div class="product-desc">Atetuer mi a ultricies massa<br>est sed nisl Class aptent</div></div>
<svg class="chev" style="left:263px" viewBox="0 0 36 36" aria-hidden="true"><circle cx="18" cy="18" r="18" fill="#fff"/><path d="M12 15 L18 21 L24 15" stroke="#2f9a2a" stroke-width="3" fill="none"/></svg>
<svg class="chev" style="left:485px" viewBox="0 0 36 36" aria-hidden="true"><circle cx="18" cy="18" r="18" fill="#fff"/><path d="M12 15 L18 21 L24 15" stroke="#2f9a2a" stroke-width="3" fill="none"/></svg>
<svg class="chev" style="left:698px" viewBox="0 0 36 36" aria-hidden="true"><circle cx="18" cy="18" r="18" fill="#fff"/><path d="M12 15 L18 21 L24 15" stroke="#2f9a2a" stroke-width="3" fill="none"/></svg>

<section class="greenery">
  <div class="greenery-photo" role="img" aria-label="Cannabis buds and amber oil bottles on a rustic wooden table"></div>
  <h2 class="abs section-title" style="left:173px;top:1782px;font-size:28px;color:var(--green-text)">Our Greenery</h2>
  <p class="abs lead" style="left:178px;top:1832px;width:390px">Integer congue augue et malesuada iaculis ipsum dui aliquet felis at cursus magna nisl nec elit</p>
  <p class="abs copy" style="left:178px;top:1886px;width:392px">Aliquam sit amet porttitor mattis enim in massa libero interdum nec interdum vel blandit sed nulla in ullamcorper est eget tempor cursus neque mi consectetuer mi a ultricies massa est sed nisl Class aptent</p>
  <a class="btn-orange" style="left:180px;top:2022px;width:162px;height:40px;font-size:15px">Read More</a>
</section>

<section class="paper" style="top:2200px;height:380px"></section>
<svg class="abs" style="left:0;top:2170px;width:1200px;height:70px" viewBox="0 0 1200 70" preserveAspectRatio="none" aria-hidden="true">
  <path d="M0 8 L1200 35 L1200 0 L0 0 Z" fill="#ffffff"/>
  <path d="M0 8 L1200 35 L1200 30 L0 62 Z" fill="#1f7a1c"/>
</svg>
<h2 class="abs head news-title">Newsletter Sign Up</h2>
<p class="news-copy">Aterdum vel blandit sed nulla in ullamcorper est eget tempor cursus neque mi consectetuer mi a ultricies massa est sed nisl Class aptent</p>
<form class="news-form">
  <span class="news-placeholder">Email Address</span>
  <span class="news-submit">Subscribe</span>
</form>

<section class="contact" role="img" aria-label="Dark rustic wood plank background"></section>
<svg class="abs" style="left:0;top:2550px;width:1200px;height:90px" viewBox="0 0 1200 90" preserveAspectRatio="none" aria-hidden="true">
  <path d="M0 0 L1200 0 L1200 8 L0 62 Z" fill="#f4efe5"/>
  <path d="M760 44 L1200 8 L1200 40 Z" fill="#2f9a2a"/>
</svg>
<h2 class="abs head contact-title">Contact Us</h2>

<div class="field" style="top:2744px;height:34px">Your Name</div>
<div class="field" style="top:2793px;height:35px">Email address</div>
<div class="field" style="top:2842px;height:34px">Phone</div>
<div class="field" style="top:2891px;height:71px">Message</div>
<a class="btn-submit">Submit</a>

<svg class="info-icon" style="top:2774px" viewBox="0 0 30 30" aria-hidden="true"><path d="M15 3 C10 3 7 7 7 11 C7 17 15 26 15 26 C15 26 23 17 23 11 C23 7 20 3 15 3 Z" stroke="#fff" stroke-width="1.5" fill="none"/><circle cx="15" cy="11" r="3" stroke="#fff" stroke-width="1.5" fill="none"/></svg>
<div class="info" style="top:2770px">Our Address<br><span class="val">48 Cedarline Road #4 Abbotsford BC V2S 0A1</span></div>
<svg class="info-icon" style="top:2836px" viewBox="0 0 30 30" aria-hidden="true"><path d="M6 4 L11 4 L13 10 L10 12 C11 16 14 19 18 20 L20 17 L26 19 L26 24 C26 25 25 26 24 26 C14 26 4 16 4 6 C4 5 5 4 6 4 Z" stroke="#fff" stroke-width="1.5" fill="none"/></svg>
<div class="info" style="top:2832px">Phone<br><span class="val">604.555.0187</span></div>
<svg class="info-icon" style="top:2900px" viewBox="0 0 30 30" aria-hidden="true"><rect x="3" y="7" width="24" height="16" stroke="#fff" stroke-width="1.5" fill="none"/><path d="M3 7 L15 17 L27 7" stroke="#fff" stroke-width="1.5" fill="none"/></svg>
<div class="info" style="top:2893px">Email us<br><span class="val">hello@tallowridge.example</span></div>

<span class="social" style="left:637px"></span>
<span class="social" style="left:681px"></span>
<span class="social" style="left:725px"></span>
<span class="social" style="left:769px"></span>

<footer class="site-footer">
  <nav class="footer-nav"><a href="#">Shop</a><a href="#">Investors</a><a href="#">Mission</a><a href="#">Vision</a></nav>
  <p class="footer-copy">© 2018 Tallow Ridge. All right reserved. Term of Use</p>
</footer>

</body>
</html>
```